Coffee label for coffee brand - Kiln Lane coffee

We want someone to design a label for packaging of a coffee line. The design will then be printed on stickers.

It is called Kiln Lane Coffee (logo enclosed) I want to incorporate a streetscape and the idea is that with every different coffee it will be a different colour (we have 6 varieties at the moment) with a black background. It needs to have a modern feel.

It needs to have a blank area towards the bottom for the type of coffee which we will print later on)

text to include

'Roasting exceptional coffee'

Target Market(s)

Coffee drinkers - modern feel

Font styles to use
Sans Serif

Colors
f78f20
9bcb3b
33a6d7
b768aa

Requirements
Must have
• the logo incorporated
• Space for coffee variety
• Quote' Roasting exceptional coffee'
Nice to have
• Streetscape theme incorporated - bright colour varieties (would love metallic) (on black background)

```html
<!DOCTYPE html>
<html lang="en">
<head>
<meta charset="utf-8">
<title>Kiln Lane Coffee – Variety Label</title>
<link href="https://fonts.googleapis.com/css2?family=Josefin+Sans:wght@400;600&display=swap" rel="stylesheet">
<style>
  :root {
    --page-bg: #d9d9d9;
    --label-black: #111111;
    --silver-light: #f2f2f2;
    --silver-mid: #c9c9c9;
    --silver-dark: #9a9a9a;
    --logo-ink: #3a3a3a;
    --band-brown: #2a1a12;
    --band-edge: #4a3224;
    --band-text: #e8e2dc;
    --bean-dark: #3b2519;
    --bean-mid: #5a3b28;
    --cup-light: #e9e4df;
    --cup-mid: #b8977a;
    --variety-orange: #f78f20;
    --variety-orange-deep: #d9661a;
    --variety-text: #e6e6e6;
    --weight-box: #1c1410;
  }
  * { box-sizing: border-box; margin: 0; padding: 0; }
  html, body { width: 1200px; height: 800px; overflow: hidden; }
  body {
    background: var(--page-bg);
    font-family: "Josefin Sans", sans-serif;
    display: flex;
    align-items: center;
    justify-content: center;
  }
  .label {
    position: relative;
    width: 480px;
    height: 700px;
    background: var(--label-black);
    overflow: hidden;
  }
  .logo-panel {
    height: 270px;
    background: linear-gradient(160deg, var(--silver-light) 0%, var(--silver-mid) 40%, var(--silver-dark) 70%, var(--silver-light) 100%);
    display: flex;
    align-items: center;
    justify-content: center;
  }
  .brand-name {
    font-weight: 600;
    font-size: 46px;
    line-height: 1.05;
    text-align: center;
    color: var(--logo-ink);
    letter-spacing: 1px;
  }
  .tagline-band {
    height: 60px;
    background: var(--band-brown);
    border-top: 2px solid var(--band-edge);
    border-bottom: 2px solid var(--band-edge);
    display: flex;
    align-items: center;
    justify-content: center;
  }
  .tagline {
    font-weight: 400;
    font-size: 21px;
    letter-spacing: 1.5px;
    text-transform: uppercase;
    color: var(--band-text);
  }
  .bean-strip {
    height: 115px;
    background: linear-gradient(90deg, var(--bean-dark), var(--bean-mid) 50%, var(--bean-dark));
  }
  .cup-image {
    position: absolute;
    left: 161px;
    top: 356px;
    width: 158px;
    height: 158px;
    background: linear-gradient(160deg, var(--cup-light), var(--cup-mid));
    z-index: 2;
  }
  .variety-panel {
    position: relative;
    height: 255px;
    background: linear-gradient(100deg, var(--variety-orange-deep), var(--variety-orange) 55%, var(--variety-orange-deep));
  }
  .variety-name {
    position: absolute;
    left: 0; right: 0;
    top: 112px;
    text-align: center;
    font-weight: 600;
    font-size: 44px;
    letter-spacing: 2px;
    color: var(--variety-text);
    text-transform: uppercase;
  }
  .net-weight {
    position: absolute;
    left: 50%;
    bottom: 0;
    transform: translateX(-50%);
    width: 82px;
    height: 40px;
    background: var(--weight-box);
    color: var(--variety-text);
    font-size: 15px;
    display: flex;
    align-items: center;
    justify-content: center;
    letter-spacing: 1px;
  }
</style>
</head>
<body>
  <main class="label">
    <header class="logo-panel">
      <p class="brand-name">Kiln Lane<br>Coffee</p>
    </header>
    <section class="tagline-band">
      <p class="tagline">Roasting exceptional coffee</p>
    </section>
    <div class="bean-strip" role="img" aria-label="Roasted coffee beans background"></div>
    <div class="cup-image" role="img" aria-label="Top view of a cup of coffee"></div>
    <section class="variety-panel">
      <p class="variety-name">Coffee Variety</p>
      <p class="net-weight">500G</p>
    </section>
  </main>
</body>
</html>
```